Business Postcard Design for Personal Training Company

Need a postcard design for my company called "Maple Stride" Colors are Navy Blue, Blue, Grey and White.

On the front I want there to be pictures and it to feature a box that says "Free Consultation + 50% off your first session!"

And somehow to feature the following phrases " Lose Weight. Gain Muscle."
"Customized Personal training using Q-Pulse, the latest technology in fitness. Reach your fitness goals in just two 25-min sessions per week"

Also want featured the following phrases (maybe on back):

"up to 18 times more effective than a conventional gym workout"

I need the back of the postcard to have all my business information:

Address: 372 Dovercrest Ave, Building B Suite 218, Costa Mesa CA 92631
Website: maple-stride.example
Phone #: (949) 555-0137
E-mail: maplestridehealth@mailbox.example

I am going to upload my logo, before and after pictures and pictures of people training on the device. Feel free to use as many/or little photos as you want.

Target Market(s)

Wealthy Adults 40+ years old looking for a personal trainer

Industry/Entity Type

Personal Trainer

Colors
0455a3
85cae6
aaaaaa
ffffff

Requirements
Must have
• At least two of the before and after photos, and two or more photos of people working out on the device.

```html
<!DOCTYPE html>
<html lang="en">
<head>
<meta charset="utf-8">
<title>Maple Stride Postcard</title>
<link href="https://fonts.googleapis.com/css2?family=Open+Sans:ital,wght@0,400;0,600;0,700;0,800;1,700&family=Oswald:wght@500;600&display=swap" rel="stylesheet">
<style>
  :root{
    --navy:#0a3f8f;
    --blue:#0455a3;
    --sky:#85cae6;
    --sky-soft:#cfe9f5;
    --grey:#aaaaaa;
    --grey-dark:#6f6f6f;
    --white:#ffffff;
    --ink:#1b1b1b;
    --stage:#e9ebee;
  }
  *{box-sizing:border-box;margin:0;padding:0}
  html,body{width:902px;height:1200px;overflow:hidden}
  body{background:var(--stage);font-family:"Open Sans",Arial,sans-serif;position:relative}

  .card{position:absolute;width:674px;height:522px;background:var(--white);overflow:hidden;box-shadow:0 6px 18px rgba(0,0,0,.18)}
  .card--front{left:114px;top:52px}
  .card--back{left:114px;top:620px}

  .photo{position:absolute}
  .brand{position:absolute;display:flex;align-items:center;gap:8px}
  .brand__mark{width:24px;height:24px;border-radius:50%;background:var(--sky)}
  .brand__name{font-weight:800;font-size:18px;color:var(--grey-dark);letter-spacing:.3px;white-space:nowrap}

  .swoosh{position:absolute;left:0;top:0}

  /* front */
  .headline{position:absolute;right:18px;top:24px;color:var(--white);font-weight:800;font-size:34px;line-height:1.1;text-align:right;letter-spacing:.2px}
  .offer{position:absolute;left:254px;top:214px;width:140px;height:140px;border-radius:50%;background:var(--white);border:6px solid var(--sky);display:flex;flex-direction:column;align-items:center;justify-content:center;text-align:center;color:var(--navy);font-family:"Oswald",sans-serif}
  .offer__line{font-size:16px;font-weight:600;line-height:1.05}
  .offer__plus{font-size:20px;font-weight:500;line-height:.9}
  .offer__big{font-size:19px;font-weight:600;line-height:1.1}
  .offer__small{font-family:"Open Sans",sans-serif;font-size:7.5px;font-weight:700;line-height:1.2}
  .results{position:absolute;top:336px;display:flex;gap:6px;padding:8px 6px 0;background:var(--blue);height:126px;border-radius:2px}
  .results__item{display:flex;flex-direction:column;align-items:center;gap:4px}
  .results__photo{width:46px;height:94px;border:2px solid var(--white);border-radius:3px}
  .results__label{font-size:9.5px;font-weight:700;color:var(--white)}
  .benefits{position:absolute;left:382px;top:374px;width:284px;list-style:none;color:var(--navy);font-weight:700;font-style:italic;font-size:13px;line-height:1.3}
  .benefits li{position:relative;padding-left:16px;margin-bottom:12px}
  .benefits li::before{content:"";position:absolute;left:1px;top:5px;width:8px;height:8px;border-radius:50%;background:var(--white)}
  .band{position:absolute;left:0;bottom:0;width:100%;height:38px;background:linear-gradient(180deg,#c9c9c9,#8e8e8e 55%,#b4b4b4)}

  /* back */
  .claim{position:absolute;left:28px;top:256px;display:flex;align-items:center;gap:10px;font-family:"Oswald",sans-serif}
  .claim__count{display:flex;flex-direction:column;align-items:center;color:var(--ink);line-height:1}
  .claim__upto{font-size:15px;color:var(--blue);font-weight:600}
  .claim__num{font-size:50px;font-weight:600;line-height:.95}
  .claim__times{font-size:15px;color:var(--blue);font-weight:600}
  .claim__main{font-size:36px;font-weight:600;color:var(--ink);line-height:1}
  .claim__sub{font-size:14px;font-weight:500;color:var(--blue);line-height:1.2}
  .contact{position:absolute;left:0;top:354px;width:300px;height:116px;background:linear-gradient(90deg,var(--sky) 0%,var(--sky-soft) 100%);padding:16px 0 0 16px;color:var(--ink)}
  .contact__row{display:flex;align-items:center;gap:6px;font-size:10.5px;line-height:1.25;margin-bottom:4px}
  .contact__row--phone{font-size:17px;font-weight:700;margin-bottom:6px}
  .contact__row svg{flex:none}
  .contact__row--addr{align-items:flex-start}
  .portrait{position:absolute;left:254px;top:350px;width:124px;height:124px;border-radius:50%;border:4px solid var(--white);box-shadow:0 0 0 3px var(--blue);background:radial-gradient(circle at 50% 45%,#d9dfe4,#8fa6b8)}
  .stamp{position:absolute;left:540px;top:40px;width:106px;height:108px;border:2px solid #c9c9c9}
  .address-line{position:absolute;left:392px;width:250px;height:1px;background:#9a9a9a}
</style>
</head>
<body>

<section class="card card--front">
  <svg class="swoosh" width="674" height="522" viewBox="0 0 674 522" aria-hidden="true">
    <defs>
      <linearGradient id="sky" x1="0" x2="1"><stop offset="0" stop-color="#e3f2f9"/><stop offset="1" stop-color="#5fb2df"/></linearGradient>
    </defs>
    <path d="M340 330 H674 V484 H380 Z" fill="url(#sky)"/>
    <path d="M432 0 H674 V116 H372 C390 70 408 30 432 0 Z" fill="var(--blue)"/>
  </svg>

  <div class="brand" style="left:40px;top:46px"><span class="brand__mark"></span><span class="brand__name">Maple Stride</span></div>

  <h1 class="headline">LOSE WEIGHT<br>GAIN MUSCLE</h1>

  <div class="photo" role="img" aria-label="Smiling trainer and client exercising with dumbbells on the training device in a studio" style="left:0;top:118px;width:330px;height:214px;background:linear-gradient(135deg,#7b8ea3,#c9d4de 50%,#4f78a8)"></div>
  <div class="photo" role="img" aria-label="Two women training on the device on a rooftop lawn overlooking a harbor" style="left:340px;top:118px;width:334px;height:212px;background:linear-gradient(180deg,#c7ced6 0%,#9aa8ae 40%,#5f7b55 75%,#6e9a4f 100%)"></div>

  <svg class="swoosh" width="674" height="522" viewBox="0 0 674 522" aria-hidden="true">
    <path d="M334 330 C336 380 350 430 366 484 L300 484 L300 330 Z" fill="var(--white)"/>
    <path d="M420 0 C340 100 300 300 378 484" fill="none" stroke="#b8b8b8" stroke-width="10"/>
    <path d="M434 0 C354 100 314 300 392 484" fill="none" stroke="var(--blue)" stroke-width="5"/>
    <rect x="0" y="110" width="330" height="5" fill="var(--blue)"/>
    <rect x="0" y="332" width="330" height="3" fill="var(--blue)"/>
  </svg>

  <div class="offer">
    <span class="offer__line">FREE</span>
    <span class="offer__line">CONSULTATION</span>
    <span class="offer__plus">+</span>
    <span class="offer__big">50% OFF</span>
    <span class="offer__small">ON YOUR FIRST SESSION!</span>
  </div>

  <div class="results" style="left:22px">
    <div class="results__item"><div class="results__photo" role="img" aria-label="Client before training, front view" style="background:linear-gradient(#e7e1da,#b9a898)"></div><span class="results__label">BEFORE</span></div>
    <div class="results__item"><div class="results__photo" role="img" aria-label="Client after training, front view" style="background:linear-gradient(#e7e1da,#8c7c70)"></div><span class="results__label">AFTER</span></div>
  </div>
  <div class="results" style="left:146px">
    <div class="results__item"><div class="results__photo" role="img" aria-label="Client before training, side view" style="background:linear-gradient(#eeeeee,#b7c2cc)"></div><span class="results__label">BEFORE</span></div>
    <div class="results__item"><div class="results__photo" role="img" aria-label="Client after training, side view" style="background:linear-gradient(#eeeeee,#6d6d6d)"></div><span class="results__label">AFTER</span></div>
  </div>

  <ul class="benefits">
    <li>Customized Personal training using Q-Pulse, the latest technology in fitness.</li>
    <li>Reach your fitness goals in just two 25-min sessions per week</li>
  </ul>

  <div class="band"></div>
</section>

<section class="card card--back">
  <div class="photo" role="img" aria-label="Woman jumping in a training suit beside a trainer at the device on a rooftop above a harbor" style="left:0;top:0;width:350px;height:246px;background:linear-gradient(180deg,#cfd5db 0%,#a4adb0 38%,#6f8a5e 70%,#5d8a45 100%)"></div>

  <svg class="swoosh" width="674" height="522" viewBox="0 0 674 522" aria-hidden="true">
    <path d="M0 246 Q180 222 330 236 L320 250 Q170 238 0 258 Z" fill="var(--sky)"/>
    <path d="M330 0 Q362 170 346 352" fill="none" stroke="var(--blue)" stroke-width="12"/>
    <path d="M346 0 Q376 170 360 352" fill="none" stroke="var(--sky)" stroke-width="3"/>
  </svg>

  <div class="claim">
    <div class="claim__count">
      <span class="claim__upto">UP TO</span>
      <span class="claim__num">18</span>
      <span class="claim__times">TIMES</span>
    </div>
    <div>
      <div class="claim__main">MORE EFFECTIVE</div>
      <div class="claim__sub">THAN A CONVENTIONAL GYM WORKOUT</div>
    </div>
  </div>

  <div class="contact">
    <div class="contact__row contact__row--phone">
      <svg width="14" height="14" viewBox="0 0 24 24"><circle cx="12" cy="12" r="11" fill="none" stroke="#1b1b1b" stroke-width="2"/><path d="M8 6l2 3-1.5 1.5a8 8 0 004 4L14 13l3 2-1 2c-5 0-9-4-9-9z" fill="#1b1b1b"/></svg>
      (949) 555-0137
    </div>
    <div class="contact__row contact__row--addr">
      <svg width="10" height="13" viewBox="0 0 10 14"><path d="M5 0a5 5 0 015 5c0 4-5 9-5 9S0 9 0 5a5 5 0 015-5z" fill="var(--blue)"/><circle cx="5" cy="5" r="2" fill="#fff"/></svg>
      <span>372 Dovercrest Ave, Building B Suite 218,<br>Costa Mesa CA 92631</span>
    </div>
    <div class="contact__row">
      <svg width="10" height="8" viewBox="0 0 12 9"><rect width="12" height="9" fill="var(--blue)"/><path d="M0 0l6 5 6-5" fill="none" stroke="#fff"/></svg>
      maplestridehealth@mailbox.example
    </div>
    <div class="contact__row">
      <svg width="10" height="10" viewBox="0 0 12 12"><circle cx="6" cy="6" r="5.5" fill="none" stroke="var(--blue)"/><path d="M0.5 6h11M6 .5c3 3 3 8 0 11M6 .5c-3 3-3 8 0 11" fill="none" stroke="var(--blue)" stroke-width=".8"/></svg>
      www.maple-stride.example
    </div>
  </div>
  <div class="portrait" role="img" aria-label="Trainer holding dumbbells in the studio"></div>

  <div class="brand" style="left:378px;top:60px"><span class="brand__mark"></span><span class="brand__name" style="font-size:16px">Maple Stride</span></div>

  <div class="stamp"></div>
  <div class="address-line" style="top:244px"></div>
  <div class="address-line" style="top:286px"></div>
  <div class="address-line" style="top:332px"></div>
</section>

</body>
</html>
```